Carton Box Packaging For Motorcycle Electric Regulator - Verosta Brand

Packaging Dimensions: 7cm (H) x 6cm (W) x 2.5cm (D)
We would like to design a genuine Carton box Packaging for motorcycle electric regulator.
This is a sensitive part of the motorcycle, so we need the packaging to reflect elegant impression.
Verosta, is one of the leading companies for manufacturing Motorcycles, located in Egypt. Our company is offering high-quality products, the best in the local market, with very competitive prices.
We have a limited time to get this project done, So we Highly appreciate receiving your designs ASAP.
Target Market(s)
Motorcycle Parts Buyers
Font styles to use
Colors
Designer to choose colors to be used in the design.
Look and feel
Each slider illustrates characteristics of the customer's brand and the style your logo design should communicate.

```html
<!DOCTYPE html>
<html lang="en">
<head>
<meta charset="utf-8">
<title>Verosta Motorcycle Regulator – Box Net</title>
<link href="https://fonts.googleapis.com/css2?family=Baloo+2:wght@800&display=swap" rel="stylesheet">
<style>
  :root {
    --stage: #f2f2f2;
    --white: #ffffff;
    --paper-shade: #e6e7ea;
    --brand-red: #e3161f;
    --brand-red-deep: #b80f17;
    --brand-blue: #0f4fa8;
    --brand-blue-light: #1c8fe0;
    --brand-blue-deep: #0a3c8c;
    --ink-dark: #3a1a1a;
    --logo-grey: #2b2b2b;
    --fold: rgba(255,255,255,.35);
  }
  * { margin: 0; padding: 0; box-sizing: border-box; }
  html, body {
    width: 1200px; height: 1200px; overflow: hidden;
    background: var(--stage);
  }
  .canvas { position: relative; width: 1200px; height: 1200px; }
  .net {
    position: absolute; left: 150px; top: 160px;
    width: 880px; height: 830px;
  }
  .panel {
    position: absolute; overflow: hidden;
    background: linear-gradient(135deg, var(--brand-blue-light) 0%, var(--brand-blue) 55%, var(--brand-blue-deep) 100%);
  }
  .panel-side  { left: 0;     top: 0;     width: 180px; height: 650px; border-right: 1px dashed var(--fold); }
  .panel-top   { left: 180px; top: 0;     width: 700px; height: 650px; }
  .panel-front { left: 180px; top: 650px; width: 700px; height: 180px; border-top: 1px dashed var(--fold); }
  .panel-art { position: absolute; inset: 0; }

  .product-title {
    position: absolute;
    font-family: "Baloo 2", sans-serif; font-weight: 800;
    color: var(--brand-red); line-height: .82;
    -webkit-text-stroke: 3px var(--ink-dark);
    paint-order: stroke fill;
    white-space: nowrap;
  }
  .product-title .line-small { display: block; }
  .product-title .line-large { display: block; }

  .panel-top .product-title { left: 55px; top: 462px; }
  .panel-top .line-small { font-size: 62px; padding-left: 36px; }
  .panel-top .line-large { font-size: 124px; }

  .panel-front .product-title { left: 110px; top: 22px; }
  .panel-front .line-small { font-size: 50px; padding-left: 30px; }
  .panel-front .line-large { font-size: 100px; }

  .panel-side .product-title {
    left: 90px; top: 325px;
    transform: translate(-50%, -50%) rotate(-90deg);
  }
  .panel-side .line-small { font-size: 50px; padding-left: 30px; }
  .panel-side .line-large { font-size: 100px; }

  .brand-mark {
    position: absolute; left: 250px; top: 400px;
    display: flex; align-items: center; gap: 12px;
  }
  .brand-dot { width: 40px; height: 40px; border-radius: 50%; background: var(--logo-grey); }
  .brand-name {
    font-family: "Baloo 2", sans-serif; font-weight: 800;
    font-size: 32px; color: var(--logo-grey); line-height: 1;
  }
</style>
</head>
<body>
<main class="canvas">
  <div class="net" aria-label="Verosta motorcycle regulator box net">

    <section class="panel panel-side" role="img" aria-label="Side panel with flowing blue wave-line pattern">
      <h2 class="product-title">
        <span class="line-small">motorcycle</span>
        <span class="line-large">regulator</span>
      </h2>
    </section>

    <section class="panel panel-top">
      <svg class="panel-art" viewBox="0 0 700 650" width="700" height="650">
        <defs>
          <linearGradient id="paperFade" x1="0" y1="0" x2="1" y2="1">
            <stop offset="0" stop-color="var(--white)"/>
            <stop offset="1" stop-color="var(--paper-shade)"/>
          </linearGradient>
          <linearGradient id="redBand" x1="0" y1="0" x2="1" y2="0">
            <stop offset="0" stop-color="var(--brand-red-deep)"/>
            <stop offset=".5" stop-color="var(--brand-red)"/>
            <stop offset="1" stop-color="var(--brand-red-deep)"/>
          </linearGradient>
        </defs>
        <rect class="wave-field" width="700" height="650" fill="transparent"
              role="img" aria-label="Flowing blue wave-line pattern"/>
        <path class="white-stripe" d="M0 250 C 200 320 450 370 700 400 L700 0 L0 0 Z" fill="var(--white)"/>
        <path class="red-swoosh" d="M0 230 C 200 300 450 350 700 378 L700 0 L0 0 Z" fill="url(#redBand)"/>
        <path class="white-panel" d="M0 120 C 200 170 450 205 700 215 L700 0 L0 0 Z" fill="url(#paperFade)"/>
        <rect class="rider-illustration" x="110" y="150" width="200" height="150" rx="18"
              fill="var(--brand-blue-light)" opacity=".4"
              role="img" aria-label="Line illustration of a rider on a motorcycle"/>
        <rect class="regulator-photo" x="330" y="40" width="260" height="160" rx="12"
              fill="#3a3a3a" opacity=".85"
              role="img" aria-label="Photo of the black regulator unit with its wiring connector"/>
      </svg>
      <div class="brand-mark">
        <span class="brand-dot"></span>
        <span class="brand-name">Verosta</span>
      </div>
      <h1 class="product-title">
        <span class="line-small">motorcycle</span>
        <span class="line-large">regulator</span>
      </h1>
    </section>

    <section class="panel panel-front" role="img" aria-label="Front panel with flowing blue wave-line pattern">
      <h2 class="product-title">
        <span class="line-small">motorcycle</span>
        <span class="line-large">regulator</span>
      </h2>
    </section>

  </div>
</main>
</body>
</html>
```